Graniteway Surface Works, Inc. Business Card

New business, we do epoxy, polishing concrete, underlayment, fluid applied flooring, sound proofing, double sided, will need 3 sets of cards with 3 different names and phone numbers.
Company: Graniteway Surface Works, Inc.
Address and Phone: 6339 Charlotte Pike PMB 2183Nashville, TN 38514
(615) 418-3927
www.granitewaysurfaceworks.example

Target Market(s)

General Contractors, Contractors, Architects

Contact Information for Business Card

1st Card: Devon Halvorsen C. 708.214.5873 e. devon@granitewaysurfaceworks.example
Vice President
2nd Card: Morgan Prescoe C. 708.389.6145 e. morgan@granitewaysurfaceworks.example
President
3rd Card: Bo Vu C. 405.631.8207 e. bo@granitewaysurfaceworks.example
Managing Partner

Font styles to use
Serif
Sans Serif

Requirements
Must have
• Professional Clean Design, Implement colors from Logo or nicely contrasting
Nice to have
• N/A

```html
<!DOCTYPE html>
<html lang="en">
<head>
<meta charset="utf-8">
<title>Graniteway Surface Works, Inc. Business Card</title>
<link rel="stylesheet" href="https://fonts.googleapis.com/css2?family=Poppins:wght@400;500;700&display=swap">
<style>
  :root {
    --brand-blue: #0a63b3;
    --brand-green: #6a9e3f;
    --ink: #1d1d1f;
    --paper: #ffffff;
    --backdrop: #e6e7ea;
  }
  * { box-sizing: border-box; margin: 0; padding: 0; }
  html, body { width: 1200px; height: 1200px; overflow: hidden; }
  body {
    background: var(--backdrop);
    font-family: "Poppins", sans-serif;
    display: flex;
    flex-direction: column;
    align-items: center;
    justify-content: center;
    gap: 60px;
  }
  .card {
    width: 840px;
    height: 480px;
    box-shadow: 0 10px 30px rgba(0,0,0,.18);
    position: relative;
  }
  .card--front {
    background: var(--brand-blue);
    display: flex;
    align-items: center;
    justify-content: center;
  }
  .wordmark {
    display: flex;
    align-items: center;
    gap: 16px;
    font-weight: 700;
    line-height: 1.05;
  }
  .wordmark__square { width: 34px; height: 34px; flex: none; }
  .card--front .wordmark { color: var(--paper); font-size: 40px; }
  .card--front .wordmark__square { background: var(--paper); }

  .card--back {
    background: var(--paper);
    display: flex;
    align-items: center;
  }
  .card__brand {
    width: 370px;
    display: flex;
    justify-content: center;
    padding-left: 30px;
  }
  .card--back .wordmark { color: var(--ink); font-size: 34px; }
  .card--back .wordmark__square { background: var(--brand-blue); width: 30px; height: 30px; }
  .card__divider {
    width: 2px;
    height: 230px;
    background: var(--brand-blue);
  }
  .contact { padding-left: 50px; color: var(--ink); }
  .contact__name {
    font-weight: 700;
    font-size: 24px;
    letter-spacing: .5px;
    text-transform: uppercase;
  }
  .contact__title {
    font-size: 18px;
    color: var(--brand-green);
    display: flex;
    align-items: center;
    gap: 10px;
    margin-bottom: 14px;
  }
  .contact__title::before {
    content: "";
    width: 6px; height: 14px;
    background: var(--brand-blue);
  }
  .contact__address { font-size: 16px; line-height: 1.4; margin-bottom: 14px; }
  .contact__list { list-style: none; font-size: 16px; line-height: 1.75; }
  .contact__list li { display: flex; align-items: center; gap: 12px; }
  .contact__list svg { width: 16px; height: 16px; flex: none; fill: none; stroke: var(--brand-green); stroke-width: 2; }
  .contact__web-domain { color: var(--brand-blue); }
</style>
</head>
<body>
  <section class="card card--front" aria-label="Card front">
    <div class="wordmark"><span class="wordmark__square"></span><span>Graniteway<br>Surface Works</span></div>
  </section>

  <section class="card card--back" aria-label="Card back">
    <div class="card__brand">
      <div class="wordmark"><span class="wordmark__square"></span><span>Graniteway<br>Surface Works</span></div>
    </div>
    <div class="card__divider"></div>
    <div class="contact">
      <h1 class="contact__name">Devon Halvorsen</h1>
      <p class="contact__title">Vice President</p>
      <p class="contact__address">4812 Wendover Ridge PMB 7416<br>Nashville, TN 38514</p>
      <ul class="contact__list">
        <li><svg viewBox="0 0 16 16"><path d="M3 2h3l1 4-2 1a9 9 0 0 0 4 4l1-2 4 1v3c0 1-1 1-2 1A12 12 0 0 1 2 4c0-1 0-2 1-2z"/></svg>(615) 418-3927</li>
        <li><svg viewBox="0 0 16 16"><rect x="4" y="1.5" width="8" height="13" rx="1.5"/></svg>708.214.5873</li>
        <li><svg viewBox="0 0 16 16"><rect x="1.5" y="3.5" width="13" height="9"/><path d="M1.5 3.5 8 9l6.5-5.5"/></svg>devon@granitewaysurfaceworks.example</li>
        <li><svg viewBox="0 0 16 16"><circle cx="8" cy="8" r="6.5"/><path d="M1.5 8h13M8 1.5c-3 3.5-3 9.5 0 13M8 1.5c3 3.5 3 9.5 0 13"/></svg><span>www.<span class="contact__web-domain">granitewaysurfaceworks</span>.example</span></li>
      </ul>
    </div>
  </section>
</body>
</html>
```